Business card design needed

Design:
Want the logo/design to have an enviromental feel
Simple look not to busy

Company Info:
Pre purchase building and pest inspections
Registered building practitoner DB-U 58147 (please include building commission logo in design)

Industry/Entity Type

Building

Contact Information for Business Card

Company name:
Fernvale Building and Pest inspections

Inspectors:
Dean Harker 0451 278 914
Greg Sutcliffe 0419 562 843
Email: fernvalebpi@mailpost.example

```html
<!DOCTYPE html>
<html lang="en">
<head>
<meta charset="UTF-8">
<title>Fernvale Building and Pest inspections – Business Card</title>
<link href="https://fonts.googleapis.com/css2?family=Lilita+One&family=Roboto+Condensed:wght@300;400&display=swap" rel="stylesheet">
<style>
  :root {
    --page-bg: #e9e6e2;
    --card-bg: #fbfbfa;
    --earth-brown: #3a2416;
    --ink: #2b2b2b;
    --reg-blue: #26368f;
    --title-white: #ffffff;
  }
  * { margin: 0; padding: 0; box-sizing: border-box; }
  html, body {
    width: 1200px;
    height: 900px;
    overflow: hidden;
    background: var(--page-bg);
  }
  .canvas {
    width: 1200px;
    height: 900px;
    display: flex;
    align-items: center;
    justify-content: center;
  }
  .business-card {
    position: relative;
    width: 460px;
    height: 800px;
    background: var(--card-bg);
    box-shadow: 0 6px 22px rgba(0,0,0,0.18);
    overflow: hidden;
    font-family: "Roboto Condensed", "Arial Narrow", sans-serif;
    color: var(--ink);
  }

  /* Registration block */
  .registration {
    position: absolute;
    top: 56px;
    left: 40px;
    right: 40px;
    height: 150px;
  }
  .registration-seal {
    position: absolute;
    right: 6px;
    top: 0;
    width: 104px;
    height: 104px;
    border-radius: 50%;
    border: 4px solid var(--reg-blue);
    opacity: 0.75;
  }
  .registration-number {
    position: absolute;
    left: 0;
    bottom: 0;
    font-size: 17px;
    font-weight: 400;
    color: var(--reg-blue);
  }

  /* Service line */
  .services {
    position: absolute;
    top: 318px;
    left: 40px;
    right: 30px;
    font-size: 22px;
    font-weight: 400;
    line-height: 1.25;
  }
  .services .email {
    display: block;
    padding-left: 30px;
    font-size: 19px;
    font-weight: 300;
  }

  /* Title band */
  .title-band {
    position: absolute;
    top: 392px;
    left: 0;
    right: 0;
    height: 140px;
    background: var(--earth-brown);
    padding: 18px 30px 0 40px;
  }
  .company-name {
    font-family: "Lilita One", "Arial Black", sans-serif;
    font-weight: 400;
    font-size: 40px;
    line-height: 1.12;
    color: var(--title-white);
    letter-spacing: 0.5px;
  }
  .skyline {
    position: absolute;
    top: 532px;
    left: 0;
    right: 0;
    height: 70px;
    background: linear-gradient(to bottom, var(--earth-brown) 0%, rgba(58,36,22,0.55) 45%, rgba(58,36,22,0) 100%);
  }

  /* Inspectors */
  .inspectors {
    position: absolute;
    left: 40px;
    right: 40px;
    bottom: 48px;
    height: 120px;
  }
  .inspector {
    position: absolute;
    font-size: 22px;
    font-weight: 400;
    line-height: 1.2;
  }
  .inspector .phone {
    display: block;
    font-weight: 300;
  }
  .inspector--greg { left: 0; top: 0; }
  .inspector--dean { right: 0; bottom: 0; }
</style>
</head>
<body>
  <main class="canvas">
    <article class="business-card">
      <section class="registration">
        <div class="registration-seal" role="img" aria-label="Building commission seal"></div>
        <p class="registration-number">Registered building practitioner DB-U 58147</p>
      </section>

      <p class="services">Pre purchase building and pest inspections
        <span class="email">email: fernvalebpi@mailpost.example</span>
      </p>

      <header class="title-band">
        <h1 class="company-name">Fernvale Building &amp;<br>Pest inspections</h1>
      </header>
      <div class="skyline" role="img" aria-label="City skyline silhouette"></div>

      <section class="inspectors">
        <p class="inspector inspector--greg">Greg Sutcliffe<span class="phone">0419 562 843</span></p>
        <p class="inspector inspector--dean">Dean Harker<span class="phone">0451 278 914</span></p>
      </section>
    </article>
  </main>
</body>
</html>
```